Halvern Stationary Design

We're seeking a fresh and modern design for our stationery that captures the essence of our Real Estate brand. The current design, while functional, lacks visual appeal. We're looking for a more attractive and engaging design that showcases our professionalism and expertise in the real estate industry. I am attaching the current letter head and an image with a letter "P" as logo.

Target Market(s)

Real Estate Sales and Rentals

Industry/Entity Type

Real Estate

Requirements
Nice to have
• The owner seems to like the letter "P"

```html
<!DOCTYPE html>
<html lang="en">
<head>
<meta charset="UTF-8">
<title>Halvern Property Solutions – Letterhead</title>
<link href="https://fonts.googleapis.com/css2?family=Poppins:ital,wght@0,400;0,500;0,600;0,700;1,400&display=swap" rel="stylesheet">
<style>
  :root {
    --backdrop: #282c3b;
    --paper: #ededee;
    --ink: #3d4566;
    --ink-dark: #222633;
    --ink-muted: #8a8fa3;
    --accent-link: #5a5f9c;
    --watermark: #dcdde2;
    --rule: #3d4566;
  }
  * { box-sizing: border-box; margin: 0; padding: 0; }
  html, body {
    width: 1200px;
    height: 800px;
    overflow: hidden;
    background: var(--backdrop);
    font-family: "Poppins", sans-serif;
  }
  .canvas {
    width: 1200px;
    height: 800px;
    display: flex;
    align-items: center;
    justify-content: center;
  }
  .letterhead {
    position: relative;
    width: 537px;
    height: 760px;
    background: var(--paper);
    color: var(--ink);
    padding: 44px 52px 0;
    overflow: hidden;
  }
  .watermark {
    position: absolute;
    left: 140px;
    top: 250px;
    width: 300px;
    height: 300px;
    border-radius: 50%;
    background: var(--watermark);
    opacity: 0.6;
  }
  .brand {
    position: relative;
    text-align: center;
  }
  .brand-dot {
    display: block;
    width: 46px;
    height: 46px;
    margin: 0 auto 8px;
    border-radius: 50%;
    background: var(--ink);
  }
  .brand-name {
    font-size: 17px;
    font-weight: 600;
    color: var(--ink);
    letter-spacing: 0.2px;
  }
  .brand-contact {
    margin-top: 3px;
    font-size: 7.5px;
    font-style: normal;
    line-height: 1.45;
    color: var(--ink-dark);
  }
  .brand-contact .web {
    color: var(--accent-link);
    font-weight: 500;
  }
  .brand-contact .phones { font-weight: 600; }
  .letter-body {
    position: relative;
    margin-top: 74px;
    font-size: 7.6px;
    line-height: 1.62;
    color: var(--ink);
  }
  .salutation {
    font-weight: 700;
    margin-bottom: 8px;
  }
  .letter-body p { margin-bottom: 13px; text-align: justify; }
  .letter-body p.salutation { text-align: left; }
  .sender {
    position: relative;
    margin-top: 26px;
    color: var(--ink);
  }
  .sender-from { font-size: 8.5px; font-style: italic; }
  .sender-name { font-size: 11px; font-weight: 700; line-height: 1.1; }
  .sender-role { font-size: 7.5px; font-style: italic; }
  .signature-mark {
    width: 110px;
    height: 20px;
    margin-top: 8px;
    background: linear-gradient(90deg, rgba(61,69,102,0.08), rgba(61,69,102,0.16), rgba(61,69,102,0.06));
  }
  .signature-line {
    width: 130px;
    border-top: 1px solid var(--rule);
    margin-top: 2px;
  }
  .signature-label {
    font-size: 7.5px;
    margin-top: 4px;
    letter-spacing: 0.3px;
  }
  .footer {
    position: absolute;
    left: 52px;
    right: 52px;
    bottom: 36px;
    display: flex;
    align-items: center;
    justify-content: space-between;
    font-size: 6.8px;
    color: var(--ink-muted);
  }
  .footer-divider {
    width: 1px;
    height: 10px;
    background: var(--ink);
  }
</style>
</head>
<body>
<main class="canvas">
  <article class="letterhead">
    <div class="watermark" aria-hidden="true"></div>

    <header class="brand">
      <span class="brand-dot" aria-hidden="true"></span>
      <h1 class="brand-name">Halvern Property Solutions</h1>
      <address class="brand-contact">
        <span>418 Linden Park Road, Suite 5, Brookfield, MA 02190</span><br>
        <span class="web">halvernhomes.example</span><br>
        <span class="phones">Phone : 555-014-2286 | Fax: 555-014-7731</span>
      </address>
    </header>

    <section class="letter-body">
      <p class="salutation">DEAR SIR,</p>
      <p>Lorem Ipsum is simply dummy text of the printing and typesetting industry. Lorem Ipsum has been the industry's standard dummy text ever since the 1500s, when an unknown printer took a galley of type and scrambled it to make a type specimen book. It has survived not only five centuries, but also the leap into electronic typesetting, remaining essentially unchanged.</p>
      <p>It was popularised in the 1960s with the release of transfer lettering sheets containing Lorem Ipsum passages, and more recently with desktop publishing tools and page layout programs including versions of Lorem Ipsum.</p>
      <p>It is a long established fact that a reader will be distracted by the readable content of a page when looking at its layout. The point of using Lorem Ipsum is that it has a more-or-less normal distribution of letters, as opposed to using 'Content here, content here', making it look like readable English. Many desktop publishing packages and web page editors now use Lorem Ipsum as their default model text, and a search for 'lorem ipsum' will uncover many web sites still in their infancy. Various versions have evolved over the years, sometimes by accident, sometimes on purpose (injected humour and the like).</p>
    </section>

    <section class="sender">
      <p class="sender-from">From,</p>
      <p class="sender-name">MARCUS DELANE</p>
      <p class="sender-role">Creative Designer</p>
      <div class="signature-mark" role="img" aria-label="Handwritten signature"></div>
      <div class="signature-line"></div>
      <p class="signature-label">SIGNATURE</p>
    </section>

    <footer class="footer">
      <span>Halvern Property Solutions</span>
      <span class="footer-divider" aria-hidden="true"></span>
      <span>The Leasing Partner</span>
      <span class="footer-divider" aria-hidden="true"></span>
      <span>Serving Local Real Estate Needs for 25+ Years</span>
    </footer>
  </article>
</main>
</body>
</html>
```